Business Card & Statioary Keystone Dwelling Survey Services
Keystone Dwelling Survey Services
Professional
Dennis Varga
President
2871 NE Juniper Ridge Ln.
Palm City, FL 34990
dvarga@keystonedwellingsurveyservices.com
www.keystonedwelingsurveyservices.com
FL State License DS8162
Along the long edge of the back of the card I would like a ruler. Also on the back I would like it to list under an INSPECTIONS heading, Pre-Sale, Pre-Purchase, 4-Point, Wind Mitigation.

```html
<!DOCTYPE html>
<html lang="en">
<head>
<meta charset="utf-8">
<title>Keystone Dwelling Survey Services – Stationery</title>
<link href="https://fonts.googleapis.com/css2?family=Cinzel:wght@400;700&family=Lato:wght@400&display=swap" rel="stylesheet">
<style>
:root{
  --backdrop:#3b3b3d;
  --paper:#ffffff;
  --navy:#27358a;
  --brown:#5b3a1f;
  --ink:#3a3a3a;
  --muted:#7a7a7a;
  --ruler:#efe6cf;
}
*{box-sizing:border-box;margin:0;padding:0}
html,body{width:1200px;height:706px;overflow:hidden}
body{background:var(--backdrop);position:relative;font-family:"Lato",sans-serif;color:var(--ink)}
.sheet{position:absolute;background:var(--paper);box-shadow:0 4px 14px rgba(0,0,0,.5);overflow:hidden}
.letterhead{top:53px;width:312px;height:404px}
.letterhead--first{left:140px}
.letterhead--second{left:508px}
.brand{font-family:"Cinzel",serif;font-weight:700;color:var(--navy);display:flex;align-items:center;gap:5px;line-height:1.05}
.brand__dot{width:9px;height:9px;border-radius:50%;background:var(--navy);flex:none}
.letterhead .brand{position:absolute;left:22px;top:20px;font-size:10px;width:150px}
.letterhead .address{position:absolute;left:22px;top:52px;font-size:5px;line-height:1.5;color:var(--muted)}
.letterhead--second .address{top:325px}
.swoosh{position:absolute;left:0;bottom:0;width:100%;display:block}
.envelope{left:840px;width:232px;position:absolute}
.envelope-back{height:98px}
.envelope-back--white{top:53px;background:#f4f4f4}
.envelope-back--brown{top:130px;background:var(--brown)}
.envelope-back--blue{top:210px;background:var(--navy)}
.envelope-back svg{position:absolute;inset:0}
.envelope-back .brand{position:absolute;left:86px;top:36px;font-size:6px;width:70px}
.envelope-back--brown .brand,.envelope-back--blue .brand{color:#fff}
.envelope-back--brown .brand__dot,.envelope-back--blue .brand__dot{background:#fff}
.envelope-front{top:338px;height:152px}
.envelope-front .address{position:absolute;left:14px;top:56px;font-size:4.5px;color:var(--muted);line-height:1.5}
.envelope-front .brand{position:absolute;left:14px;top:72px;font-size:6px;width:90px}
.card{top:504px;width:300px;height:132px}
.card--front{left:348px}
.card--back{left:660px}
.card--front .brand{position:absolute;left:16px;top:12px;font-size:9px;width:160px}
.person{position:absolute;left:16px;top:52px}
.person__name{font-family:"Cinzel",serif;font-size:11px;color:var(--ink)}
.person__title{font-family:"Cinzel",serif;font-size:6px;color:var(--ink);margin-bottom:5px}
.person__line{font-size:5px;line-height:1.45;color:var(--muted)}
.card--back .brand{position:absolute;left:12px;top:12px;font-size:8px;width:110px}
.services{position:absolute;left:130px;top:10px}
.services__heading{font-family:"Cinzel",serif;font-size:13px;color:var(--ink);margin-bottom:4px}
.services__list{list-style:none;font-family:"Cinzel",serif;font-size:8px;line-height:1.45;color:var(--ink)}
.services__list li{display:flex;align-items:center;gap:4px}
.card__web{position:absolute;left:12px;bottom:8px;font-size:6px;color:var(--ink)}
.ruler{position:absolute;right:0;top:0;width:14px;height:100%}
</style>
</head>
<body>

<!-- Letterhead, first page -->
<section class="sheet letterhead letterhead--first">
  <div class="brand"><span class="brand__dot"></span>Keystone Dwelling Survey Services</div>
  <p class="address">2871 NE Juniper Ridge Ln. Palm City, FL 34990<br>Phone: (772) 555-0148<br>dvarga@keystonedwellingsurveyservices.com</p>
  <svg class="swoosh" viewBox="0 0 312 70" height="70" aria-hidden="true">
    <path d="M0 40 Q150 10 312 8 L312 20 Q160 22 0 52Z" fill="var(--navy)"/>
    <path d="M0 52 Q160 22 312 20 L312 70 L0 70Z" fill="var(--brown)"/>
  </svg>
</section>

<!-- Letterhead, following page -->
<section class="sheet letterhead letterhead--second">
  <div class="brand"><span class="brand__dot"></span>Keystone Dwelling Survey Services</div>
  <p class="address">2871 NE Juniper Ridge Ln. Palm City, FL 34990<br>Phone: (772) 555-0148<br>dvarga@keystonedwellingsurveyservices.com</p>
  <svg class="swoosh" viewBox="0 0 312 70" height="70" aria-hidden="true">
    <path d="M0 40 Q150 10 312 8 L312 20 Q160 22 0 52Z" fill="var(--navy)"/>
    <path d="M0 52 Q160 22 312 20 L312 70 L0 70Z" fill="var(--brown)"/>
  </svg>
</section>

<!-- Envelope backs -->
<section class="sheet envelope envelope-back envelope-back--white">
  <svg viewBox="0 0 232 98" width="232" height="98" aria-hidden="true"><path d="M0 0 L116 70 L232 0" fill="#fff" stroke="#ddd"/></svg>
  <div class="brand"><span class="brand__dot"></span>Keystone Dwelling</div>
</section>
<section class="sheet envelope envelope-back envelope-back--brown">
  <svg viewBox="0 0 232 98" width="232" height="98" aria-hidden="true"><path d="M0 0 L116 70 L232 0" fill="#6a4628" stroke="#4a2e17"/></svg>
  <div class="brand"><span class="brand__dot"></span>Keystone Dwelling</div>
</section>
<section class="sheet envelope envelope-back envelope-back--blue">
  <svg viewBox="0 0 232 98" width="232" height="98" aria-hidden="true"><path d="M0 0 L116 70 L232 0" fill="#31409a" stroke="#1f2b70"/></svg>
  <div class="brand"><span class="brand__dot"></span>Keystone Dwelling</div>
</section>

<!-- Envelope front -->
<section class="sheet envelope envelope-front">
  <p class="address">2871 NE Juniper Ridge Ln. Palm City, FL 34990</p>
  <div class="brand"><span class="brand__dot"></span>Keystone Dwelling Survey Services</div>
  <svg class="swoosh" viewBox="0 0 232 36" height="36" aria-hidden="true">
    <path d="M0 20 Q110 4 232 3 L232 10 Q120 12 0 28Z" fill="var(--navy)"/>
    <path d="M0 28 Q120 12 232 10 L232 36 L0 36Z" fill="var(--brown)"/>
  </svg>
</section>

<!-- Business card front -->
<section class="sheet card card--front">
  <div class="brand"><span class="brand__dot"></span>Keystone Dwelling Survey Services</div>
  <div class="person">
    <p class="person__name">Dennis Varga</p>
    <p class="person__title">President</p>
    <p class="person__line">2871 NE Juniper Ridge Ln.</p>
    <p class="person__line">Palm City, FL 34990</p>
    <p class="person__line">Phone: (772) 555-0148</p>
    <p class="person__line">dvarga@keystonedwellingsurveyservices.com</p>
    <p class="person__line">FL State License DS8162</p>
  </div>
  <svg class="swoosh" viewBox="0 0 300 34" height="34" aria-hidden="true">
    <path d="M120 34 Q220 4 300 0 L300 8 Q230 12 150 34Z" fill="var(--navy)"/>
    <path d="M150 34 Q230 12 300 8 L300 34Z" fill="var(--brown)"/>
  </svg>
</section>

<!-- Business card back -->
<section class="sheet card card--back">
  <div class="brand"><span class="brand__dot"></span>Keystone Dwelling Survey Services</div>
  <div class="services">
    <h2 class="services__heading">Inspections:</h2>
    <ul class="services__list">
      <li><svg width="8" height="8" viewBox="0 0 8 8" aria-hidden="true"><path d="M1 4 L3 6 L7 1" fill="none" stroke="var(--navy)" stroke-width="1.4"/></svg>Pre-Sale</li>
      <li><svg width="8" height="8" viewBox="0 0 8 8" aria-hidden="true"><path d="M1 4 L3 6 L7 1" fill="none" stroke="var(--navy)" stroke-width="1.4"/></svg>Pre-Purchase</li>
      <li><svg width="8" height="8" viewBox="0 0 8 8" aria-hidden="true"><path d="M1 4 L3 6 L7 1" fill="none" stroke="var(--navy)" stroke-width="1.4"/></svg>4-Point</li>
      <li><svg width="8" height="8" viewBox="0 0 8 8" aria-hidden="true"><path d="M1 4 L3 6 L7 1" fill="none" stroke="var(--navy)" stroke-width="1.4"/></svg>Wind Mitigation</li>
    </ul>
  </div>
  <p class="card__web">www.keystonedwelingsurveyservices.com</p>
  <svg class="ruler" viewBox="0 0 14 132" preserveAspectRatio="none" aria-hidden="true">
    <rect width="14" height="132" fill="var(--ruler)"/>
    <g stroke="#8a7a55" stroke-width="0.6">
      <line x1="14" y1="6" x2="6" y2="6"/><line x1="14" y1="12" x2="10" y2="12"/><line x1="14" y1="18" x2="8" y2="18"/><line x1="14" y1="24" x2="10" y2="24"/>
      <line x1="14" y1="30" x2="6" y2="30"/><line x1="14" y1="36" x2="10" y2="36"/><line x1="14" y1="42" x2="8" y2="42"/><line x1="14" y1="48" x2="10" y2="48"/>
      <line x1="14" y1="54" x2="6" y2="54"/><line x1="14" y1="60" x2="10" y2="60"/><line x1="14" y1="66" x2="8" y2="66"/><line x1="14" y1="72" x2="10" y2="72"/>
      <line x1="14" y1="78" x2="6" y2="78"/><line x1="14" y1="84" x2="10" y2="84"/><line x1="14" y1="90" x2="8" y2="90"/><line x1="14" y1="96" x2="10" y2="96"/>
      <line x1="14" y1="102" x2="6" y2="102"/><line x1="14" y1="108" x2="10" y2="108"/><line x1="14" y1="114" x2="8" y2="114"/><line x1="14" y1="120" x2="10" y2="120"/>
      <line x1="14" y1="126" x2="6" y2="126"/>
    </g>
  </svg>
</section>

</body>
</html>
```